Buch-/eBook-Cover für einen Elternratgeber
Zielgruppe
Buch: Elternratgeber
Titel: Zahlen fühlen
Untertitel: Deinem Kind den richtigen Umgang beibringen
Wir sind der ULM Verlag und suchen ein passendes Cover für unseren neuen Elternratgeber. Mit diesem Buch möchten wir Eltern unterstützen, ihren Kindern einen guten und verantwortungsvollen Umgang mit Geld zu vermitteln.
Anforderungen an das Cover-Design:
Bitte keinen Comicstil
Das Buch richtet sich an Eltern (nicht kindlich oder verspielt gestalten)
Keine direkte Darstellung von Geld (z. B. keine Münzen, Geldscheine, Sparschweine usw.)
Ob mit oder ohne Personen auf dem Cover: sind wir offen
Farbwahl und Bildsprache: gerne seriös, ansprechend und modern
Wir sind gespannt auf kreative und professionelle Vorschläge!
E-Book E-Book"
Das Design darf nicht zu überladen sein.

```html
<!DOCTYPE html>
<html lang="de">
<head>
<meta charset="utf-8">
<title>Zahlen fühlen – Elternratgeber</title>
<link rel="stylesheet" href="https://fonts.googleapis.com/css2?family=Jost:wght@500;600&display=swap">
<style>
  :root {
    --teal: #0b4655;
    --magenta: #c5077f;
    --white: #ffffff;
    --stone-light: #f1efee;
  }
  html, body {
    margin: 0;
    padding: 0;
    overflow: hidden;
    background: var(--white);
  }
  .cover {
    position: relative;
    width: 750px;
    height: 1200px;
    overflow: hidden;
    background: var(--white);
    font-family: "Jost", "Futura", sans-serif;
  }
  .hero-photo {
    position: absolute;
    left: 0; top: 0;
    width: 750px; height: 590px;
    background:
      radial-gradient(ellipse 150px 110px at 540px 480px, #aab3b6 0%, rgba(170,179,182,0) 100%),
      radial-gradient(ellipse 110px 60px at 540px 395px, #dcdcda 0%, rgba(220,220,218,0) 100%),
      radial-gradient(ellipse 110px 70px at 265px 500px, #ebe3df 0%, rgba(235,227,223,0) 100%),
      radial-gradient(ellipse 110px 60px at 130px 200px, #8fa3a8 0%, rgba(143,163,168,0) 100%),
      radial-gradient(ellipse 380px 170px at 330px 360px, #e2c0b0 0%, rgba(226,192,176,0) 100%),
      radial-gradient(ellipse 220px 260px at 700px 260px, #3f4038 0%, rgba(63,64,56,0) 100%),
      radial-gradient(ellipse 220px 80px at 470px 70px, #c9c8c0 0%, rgba(201,200,192,0) 100%),
      linear-gradient(180deg, #7b7d70 0%, #8a8a7e 30%, #c6a696 60%, #d5b5a6 100%);
  }
  .stone-band {
    position: absolute;
    left: 0; top: 604px;
    width: 750px; height: 323px;
    background:
      radial-gradient(ellipse 130px 55px at 570px 110px, #d8d6d4 0%, rgba(216,214,212,0) 100%),
      radial-gradient(ellipse 120px 40px at 280px 25px, #e0dfdd 0%, rgba(224,223,221,0) 100%),
      radial-gradient(ellipse 200px 70px at 640px 200px, #dedbd8 0%, rgba(222,219,216,0) 100%),
      radial-gradient(ellipse 180px 60px at 120px 200px, #e2dfdc 0%, rgba(226,223,220,0) 100%),
      linear-gradient(180deg, #ece6e4 0%, var(--stone-light) 60%, #f7f6f5 100%);
  }
  .title {
    position: absolute;
    left: 34px; top: 640px;
    margin: 0;
    color: var(--teal);
    font-weight: 600;
    font-size: 88px;
    line-height: 84px;
    letter-spacing: 5px;
    text-transform: uppercase;
  }
  .subtitle {
    position: absolute;
    left: 44px; top: 818px;
    margin: 0;
    color: var(--magenta);
    font-weight: 500;
    font-size: 38px;
    line-height: 45px;
    letter-spacing: 1px;
  }
  .footer-band {
    position: absolute;
    left: 0; top: 942px;
    width: 750px; height: 258px;
    background: var(--magenta);
  }
  .series-label {
    position: absolute;
    left: 422px; top: 942px;
    width: 328px; height: 60px;
    background: var(--teal);
    color: var(--white);
    display: flex;
    align-items: center;
    justify-content: center;
    font-weight: 500;
    font-size: 25px;
    letter-spacing: 2.5px;
    text-transform: uppercase;
  }
</style>
</head>
<body>
  <div class="cover">
    <div class="hero-photo" role="img" aria-label="Foto: Hände stapeln glatte graue und helle Kieselsteine zu zwei kleinen Türmen, unscharfer Naturhintergrund"></div>
    <div class="stone-band" role="img" aria-label="Blasses, aufgehelltes Foto von gestapelten Kieselsteinen als Hintergrund für den Titel"></div>
    <h1 class="title">Zahlen<br>fühlen</h1>
    <p class="subtitle">Deinem Kind den richtigen<br>Umgang beibringen</p>
    <div class="footer-band"></div>
    <div class="series-label">Elternratgeber</div>
  </div>
</body>
</html>
```